Packaging Design for Face Mask Box

We are looking for an attractive but subtle packaging design for Face Masks (for non medical use). 50pcs per box.

The brand name should be "Kelvano". We have not yet got a logo or a text selected (font) for the brand name so we are open to your ideas on how "Kelvano" could look. It could have some elements of fresh air or breathing etc so symbolize clean and healthier air or something along those lines.

The box dimensions should be 180mm (L) x 100mm (W) x 90mm (H).

The box should have a perforation on top - exactly similar to Tissue Box packs. So, in order to access the face masks, the user should tear off the perforation and extract one mask at a time.

As this is not a medical grade face mask, the product should indicate "For Non- Medical Use". Also the heading of the masks should be DISPOSABLE PROTECTIVE FACE MASKS with sub heading 3 PLY FACE MASKS WITH EAR LOOP.

We will also prefer to have the Instructions to use and Precautions which are commonly available on face mask packages. This could be printed either on the sides or on the bottom of the package. There should also be a blank space on one of the sides to print Batch No. Mfg Date and Exp Date.

The box design could have some design resemblance to our company logo which is hereby attached in high resolution. However this is not compulsory.

The following phrases could be mentioned on the box to highlight some of the product features:

Dual Charge Electrostatic fibres for extra filtration
Improved Nose Bridge Strips for better protection
Tri-layer barrier with 3 x 25 g/m2 material
In-house production of filter material for Quality Consistency

I have added 3 samples face mask box designs from other manufacturers for your reference to get an idea of the box shape etc.

If you have any more questions, please feel free to ask.

Good luck!

```html
<!DOCTYPE html>
<html lang="en">
<head>
<meta charset="utf-8">
<title>Kelvano Face Mask Box – Flat Panels</title>
<link href="https://fonts.googleapis.com/css2?family=Great+Vibes&family=Lato:wght@400;700&display=swap" rel="stylesheet">
<style>
  :root {
    --stage: #0b0c0d;
    --mint: #93f4d0;
    --mint-deep: #6fe3bd;
    --ink: #1b1d1c;
    --white: #ffffff;
    --perf: #5fc8b0;
    --maker: #2f5f8f;
  }
  html, body {
    margin: 0;
    padding: 0;
    width: 1200px;
    height: 1182px;
    overflow: hidden;
    background: var(--stage);
  }
  .canvas {
    position: relative;
    width: 1200px;
    height: 1182px;
    font-family: "Lato", sans-serif;
  }
  .panel {
    position: absolute;
    background: var(--mint);
    overflow: hidden;
    box-sizing: border-box;
  }
  .panel-top   { left: 456px; top: 236px; width: 648px; height: 360px; }
  .panel-front { left: 456px; top: 600px; width: 648px; height: 324px; }
  .panel-side  { left: 92px;  top: 600px; width: 360px; height: 324px; background: var(--mint-deep); }

  .brand {
    position: absolute;
    font-family: "Great Vibes", cursive;
    color: var(--white);
    line-height: 1.15;
    margin: 0;
    font-weight: 400;
    white-space: nowrap;
  }
  .heading, .subheading {
    position: absolute;
    margin: 0;
    text-transform: uppercase;
    color: var(--white);
    white-space: nowrap;
  }
  .heading { font-weight: 700; letter-spacing: 1px; }
  .subheading { font-weight: 400; letter-spacing: 2px; }

  .photo { position: absolute; }
  .photo-woman {
    left: 0; top: 0; width: 290px; height: 360px;
    background: linear-gradient(100deg, #d9a98d 0%, #cdb78e 40%, #c7bb93 75%, rgba(147,244,208,0) 100%);
  }
  .photo-man {
    right: 0; top: 0; width: 160px; height: 324px;
    background: linear-gradient(200deg, #3b2f2a 0%, #8a6a58 40%, #c89a7e 65%, #a9d6ec 100%);
  }

  .panel-top .brand { left: 320px; top: 14px; font-size: 96px; }
  .panel-top .heading { left: 320px; top: 134px; font-size: 14px; }
  .panel-top .subheading { left: 332px; top: 160px; font-size: 12px; }
  .perforation {
    position: absolute;
    left: 330px; top: 196px;
    width: 270px; height: 80px;
    border: 1.5px dashed var(--perf);
    border-radius: 14px;
  }
  .notice {
    position: absolute;
    right: 28px; bottom: 22px;
    margin: 0;
    font-size: 15px;
    font-weight: 700;
    letter-spacing: 2px;
    color: var(--ink);
  }

  .panel-front .brand { left: 70px; top: 4px; font-size: 100px; }
  .panel-front .heading { left: 36px; top: 128px; font-size: 16px; }
  .panel-front .subheading { left: 36px; top: 156px; font-size: 14px; }
  .features {
    position: absolute;
    left: 36px; top: 196px;
    margin: 0; padding: 0;
    list-style: none;
    font-size: 14px;
    font-weight: 700;
    line-height: 1.35;
    color: var(--ink);
  }

  .panel-side .brand { left: 50px; top: 14px; font-size: 88px; }
  .panel-side .heading { left: 40px; top: 132px; font-size: 13px; }
  .panel-side .subheading { left: 40px; top: 156px; font-size: 11px; }
  .maker {
    position: absolute;
    left: 40px; bottom: 40px;
    display: flex; align-items: center; gap: 8px;
    margin: 0;
    font-size: 13px;
    font-weight: 700;
    color: var(--maker);
  }
  .maker-mark {
    width: 14px; height: 14px;
    background: var(--maker);
  }
</style>
</head>
<body>
<main class="canvas">

  <section class="panel panel-top" aria-label="Top panel">
    <div class="photo photo-woman" role="img" aria-label="Photo of a woman with long blonde hair wearing a green three-ply face mask"></div>
    <h2 class="brand">Kelvano</h2>
    <p class="heading">Disposable Protective Face Masks</p>
    <p class="subheading">3 Ply Face Masks with Ear Loop</p>
    <div class="perforation" aria-label="Tear-off perforation"></div>
    <p class="notice">FOR NON-MEDICAL USE</p>
  </section>

  <section class="panel panel-side" aria-label="Side panel">
    <h2 class="brand">Kelvano</h2>
    <p class="heading">Disposable Protective Face Masks</p>
    <p class="subheading">3 Ply Face Masks with Ear Loop</p>
    <p class="maker"><span class="maker-mark"></span>Harvane Medical</p>
  </section>

  <section class="panel panel-front" aria-label="Front panel">
    <div class="photo photo-man" role="img" aria-label="Photo of a dark-haired man wearing a blue three-ply face mask"></div>
    <h1 class="brand">Kelvano</h1>
    <p class="heading">Disposable Protective Face Masks</p>
    <p class="subheading">3 Ply Face Masks with Ear Loop</p>
    <ul class="features">
      <li>Dual Charge Electrostatic Fibres for Extra Filtration</li>
      <li>Improved Nose Bridge Strips for Better Protection</li>
      <li>Tri-layer Barrier with 3 x 25g/m2 material</li>
      <li>In-house production of filter material</li>
      <li>for Qua;ity Consistency</li>
    </ul>
  </section>

</main>
</body>
</html>
```